Website re-design

We are a successful furnished apartment provider in Boston. We currently are working on re-designing our website www.ribtenlofts.com to make it more modern, designer look and user friendly. We hired a designer, but are not happy with the designs proposed and want to improve on them. The winning design will be paid regardless of whether we stay with our current designer or not. We want ideas and functional page links to see how it will work. Platform we have chosen is wordpress. Feel free to propose others easy for us to update and modify. We do not like Joomla on which website is currently running. We do not like flash nor long load times.
Please use photos on our website for design presentations. www.ribtenlofts.com

Target Market(s)

doctors, nurses, business men but mostly business women, some post-medical students

Industry/Entity Type

Apartment

Requirements
Must have
• Quick action button for reservation form and a notification and email forwarding system to us of reservation information by potential clients. Blog required with feedback by guests allowed, we can censor which are published. Slide shows of apartments.
Should not have
• No movies.

```html
<!DOCTYPE html>
<html lang="en">
<head>
<meta charset="utf-8">
<title>Ribten Lofts – Furnished Apartments</title>
<link href="https://fonts.googleapis.com/css2?family=Arimo:ital,wght@0,400;0,700;1,400&family=Raleway:wght@300;400&family=Tenor+Sans&display=swap" rel="stylesheet">
<style>
:root{
  --gold:#c9b27a;
  --gold-deep:#a8904f;
  --ink:#1c1c1c;
  --wood-top:#242424;
  --wood-bottom:#121212;
  --body-bg:#272727;
  --field:#7d7d7d;
  --field-edge:#5f5f5f;
  --label:#ffffff;
  --muted:#8c8c8c;
  --panel:#ffffff;
}
*{box-sizing:border-box;margin:0;padding:0}
html,body{width:844px;height:1200px;overflow:hidden}
body{position:relative;background:var(--body-bg);font-family:"Arimo",Arial,sans-serif;color:var(--label)}
.abs{position:absolute;white-space:nowrap}
.masthead{left:0;top:0;width:844px;height:447px;background:repeating-linear-gradient(90deg,rgba(255,255,255,.025) 0 2px,transparent 2px 9px),linear-gradient(var(--wood-top),var(--wood-bottom))}
.lower-bg{left:0;top:447px;width:844px;height:686px;background:radial-gradient(rgba(255,255,255,.03) 1px,transparent 1px) 0 0/4px 4px,var(--body-bg)}
.brand{left:35px;top:27px;width:230px;height:78px;border:2px solid #6a6a6a;border-radius:6px;background:linear-gradient(#555,#2a2a2a);display:flex;align-items:center;gap:12px;padding-left:14px}
.brand-dot{flex:none;width:50px;height:50px;border-radius:50%;background:var(--gold)}
.brand-name{font-family:"Raleway",sans-serif;font-weight:400;font-size:19px;letter-spacing:1px;color:var(--gold);white-space:nowrap}
.util-links{left:517px;top:14px;font-size:12px;color:var(--gold)}
.util-links span{margin:0 6px}
.pay-btn{left:733px;top:9px;width:78px;height:19px;border-radius:10px;background:linear-gradient(#f5d36a,#e2a72a);color:#1d2f6b;font:italic 700 11px "Arimo",sans-serif;text-align:center;line-height:19px}
.cards{left:731px;top:31px;display:flex;gap:3px}
.cards i{display:block;width:17px;height:11px;background:#ddd;border-radius:1px}
.phone{left:592px;top:50px;display:flex;align-items:center;gap:6px;color:var(--gold);font:700 27px "Arimo",sans-serif;letter-spacing:.5px}
.nav{left:0;top:113px;width:844px;height:45px;border-top:1px solid var(--gold-deep);border-bottom:1px solid var(--gold-deep);background:linear-gradient(#141414,#0a0a0a)}
.nav a{position:absolute;top:7px;height:30px;line-height:30px;font-size:14px;color:#fff;text-decoration:none}
.nav a.current{left:33px;width:78px;text-align:center;background:linear-gradient(#6a6a6a,#444);border-radius:3px}
.showcase{left:33px;top:166px;width:777px;height:374px;background:var(--panel);box-shadow:0 2px 8px rgba(0,0,0,.5)}
.hero-photo{left:46px;top:181px;width:536px;height:266px;background:linear-gradient(100deg,#5a3a1e 0%,#c99a58 35%,#e6c48a 55%,#a77a45 80%,#4a321c 100%)}
.dots{left:89px;top:419px;display:flex;gap:5px}
.dots i{display:block;width:12px;height:12px;border-radius:50%;background:#fff}
.dots i:first-child{background:#111}
.thumb{width:92px;height:80px;background:linear-gradient(135deg,#3a2e26,#8a6a4a 50%,#2c2c30)}
.welcome-small{left:46px;top:457px;font:300 21px "Raleway",sans-serif;color:#222}
.welcome-big{left:46px;top:485px;font:300 23px "Raleway",sans-serif;color:#222}
.welcome-tag{left:46px;top:516px;font:400 9px "Arimo",sans-serif;color:#222;letter-spacing:2.2px}
.welcome-rule{left:213px;top:460px;width:1px;height:66px;background:#bbb}
.intro{left:230px;top:459px;width:565px;font-size:10.6px;line-height:15px;color:#111;text-align:justify;white-space:normal}
.heading{font:26px "Tenor Sans",sans-serif;color:var(--gold);text-shadow:0 1px 2px #000}
.lbl{font-size:12px;color:var(--label)}
.field{background:var(--field);border:1px solid var(--field-edge);border-radius:3px;box-shadow:inset 0 1px 2px rgba(0,0,0,.4)}
.caret{position:absolute;right:1px;top:1px;width:19px;height:19px;background:#f2f2f2;border-radius:2px}
.gold-sub{font-size:15px;color:var(--gold)}
.note{font:italic 9.5px "Arimo",sans-serif;color:var(--gold-deep);text-align:right}
.terms{left:33px;top:948px;font-size:12px;color:var(--gold);display:flex;align-items:center;gap:6px}
.terms b{display:inline-block;width:14px;height:14px;border-radius:50%;background:var(--gold-deep);margin-left:8px}
.terms em{font-style:normal;color:#fff}
.captcha{left:233px;top:1015px;width:99px;height:33px;background:#fff;color:#111;font:13px "Arimo",monospace;padding:8px 4px}
.submit{left:347px;top:1020px;width:66px;height:26px;border-radius:3px;background:linear-gradient(#d9c386,#96803f);color:#fff;font:700 14px "Arimo",sans-serif;text-align:center;line-height:26px}
.footnotes{left:33px;top:1081px;width:450px;font:italic 10px/13px "Arimo",sans-serif;color:var(--gold-deep);white-space:normal}
.divider{left:489px;top:565px;width:1px;height:548px;background:#3d3d3d}
.quick{font-size:12.5px;color:#fff;display:flex;align-items:center;gap:8px}
.rule{left:535px;width:275px;height:1px;background:#444}
.testimonial{position:absolute;left:537px;width:273px;height:100px}
.testimonial .photo{position:absolute;left:0;top:0;width:74px;height:68px;background:#fff;padding:3px;box-shadow:0 1px 3px #000}
.testimonial .photo span{display:block;width:100%;height:100%;background:linear-gradient(#c9ccd0,#6b7480)}
.t-title{position:absolute;left:85px;top:0;font:700 13px "Arimo",sans-serif;color:#fff}
.t-body{position:absolute;left:85px;top:16px;width:188px;font-size:11px;line-height:13.5px;color:var(--gold-deep);text-align:justify}
.t-meta{position:absolute;left:1px;top:84px;font:italic 11px "Arimo",sans-serif;color:var(--muted)}
.t-more{position:absolute;right:0;top:84px;font:700 11px "Arimo",sans-serif;color:#fff}
.footer{left:0;top:1133px;width:844px;height:67px;background:linear-gradient(#f0f0f0,#d8d8d8)}
.footer-text{left:34px;top:1164px;font-size:11px;color:#222}
.social{top:1151px;width:46px;height:38px;border-radius:7px}
</style>
</head>
<body>
<div class="abs masthead"></div>
<div class="abs lower-bg"></div>

<header>
  <div class="abs brand"><span class="brand-dot"></span><span class="brand-name">RIBTEN LOFTS</span></div>
  <div class="abs util-links">Register<span>|</span>My Account<span>|</span>Sitemap</div>
  <div class="abs pay-btn">Pay Now</div>
  <div class="abs cards"><i></i><i></i><i></i><i></i></div>
  <div class="abs phone">
    <svg width="38" height="50" viewBox="0 0 38 50" aria-hidden="true"><path d="M10 2c3 0 5 8 5 11s-5 4-5 6c0 6 4 14 9 18 2 1 4-4 7-3s9 4 9 7-5 8-9 8C15 49 2 30 2 14 2 7 6 2 10 2z" fill="#fff"/></svg>
    <span>617 555 0148</span>
  </div>
  <nav class="abs nav">
    <a class="current" href="#">HOME</a>
    <a href="#" style="left:148px">ABOUT US</a>
    <a href="#" style="left:250px">APARTMENTS</a>
    <a href="#" style="left:370px">RESERVATIONS</a>
    <a href="#" style="left:500px">BLOG</a>
    <a href="#" style="left:573px">REVIEW</a>
    <a href="#" style="left:656px">BOSTAN</a>
    <a href="#" style="left:752px">CONTACT</a>
  </nav>
</header>

<section class="abs showcase"></section>
<div class="abs hero-photo" role="img" aria-label="Photo of a furnished apartment bedroom with warm walls and tall windows"></div>
<div class="abs dots"><i></i><i></i><i></i><i></i></div>
<div class="abs thumb" style="left:598px;top:181px" role="img" aria-label="Apartment thumbnail photo"></div>
<div class="abs thumb" style="left:705px;top:181px" role="img" aria-label="Apartment thumbnail photo"></div>
<div class="abs thumb" style="left:598px;top:274px" role="img" aria-label="Apartment thumbnail photo"></div>
<div class="abs thumb" style="left:705px;top:274px" role="img" aria-label="Apartment thumbnail photo"></div>
<div class="abs thumb" style="left:598px;top:367px" role="img" aria-label="Apartment thumbnail photo"></div>
<div class="abs thumb" style="left:705px;top:367px" role="img" aria-label="Apartment thumbnail photo"></div>
<div class="abs welcome-small">Welcome to</div>
<div class="abs welcome-big">RIBTEN LOFTS</div>
<div class="abs welcome-tag">FURNISHED APARTMENTS</div>
<div class="abs welcome-rule"></div>
<p class="abs intro">Ribten Lofts is proud to offer some of the best furnished apartments in Boston. Our locations are in the trendiest area of the city: the South End. In the South End neighborhood, you will find wonderful restaurants, theaters, cafes and artist lofts. Our short term and extended stay apartments are very, very clean. We also offer the latest designer layouts: hardwood floors, Wireless Dsl, Cable TV, flat screen in most apartments, washer and dryer, cookware, cotton linens.</p>

<h2 class="abs heading" style="left:33px;top:565px">Reservations Form</h2>
<div class="abs lbl" style="left:33px;top:605px">Name</div>
<div class="abs field" style="left:33px;top:623px;width:179px;height:22px"></div>
<div class="abs lbl" style="left:232px;top:605px">Address</div>
<div class="abs field" style="left:232px;top:623px;width:179px;height:71px"></div>
<div class="abs lbl" style="left:33px;top:656px">Work position &amp; Company *</div>
<div class="abs field" style="left:33px;top:673px;width:179px;height:22px"></div>
<div class="abs lbl" style="left:33px;top:704px">Telephone</div>
<div class="abs field" style="left:33px;top:721px;width:179px;height:22px"></div>
<div class="abs lbl" style="left:232px;top:704px">Cellphone</div>
<div class="abs field" style="left:232px;top:721px;width:179px;height:22px"></div>
<div class="abs lbl" style="left:33px;top:750px">Email</div>
<div class="abs field" style="left:33px;top:768px;width:179px;height:22px"></div>
<div class="abs gold-sub" style="left:33px;top:803px">Apartment Desired**</div>
<div class="abs lbl" style="left:33px;top:829px">Choice 1</div>
<div class="abs lbl" style="left:165px;top:829px">Choice 2</div>
<div class="abs lbl" style="left:297px;top:829px">Choice 3</div>
<div class="abs field" style="left:33px;top:846px;width:116px;height:22px"><span class="caret"></span></div>
<div class="abs field" style="left:165px;top:846px;width:116px;height:22px"><span class="caret"></span></div>
<div class="abs field" style="left:297px;top:846px;width:116px;height:22px"><span class="caret"></span></div>
<div class="abs lbl" style="left:33px;top:882px">Arrival Date</div>
<div class="abs lbl" style="left:165px;top:882px">Departure Date</div>
<div class="abs lbl" style="left:298px;top:882px">Number of Occupants</div>
<div class="abs field" style="left:33px;top:899px;width:116px;height:22px"><span class="caret"></span></div>
<div class="abs field" style="left:165px;top:899px;width:116px;height:22px"><span class="caret"></span></div>
<div class="abs field" style="left:298px;top:899px;width:179px;height:22px"></div>
<div class="abs note" style="left:298px;top:926px;width:177px">(maximum only 2 people per apartment)</div>
<div class="abs terms">I have read and accept Ribten Lofts Terms: <b></b><em>Yes</em><b></b><em>No</em></div>
<div class="abs lbl" style="left:33px;top:972px">Any Special Requests</div>
<div class="abs field" style="left:33px;top:990px;width:179px;height:51px"></div>
<div class="abs lbl" style="left:232px;top:972px">Please Enter Anti Spam Code:</div>
<div class="abs field" style="left:232px;top:990px;width:179px;height:21px"></div>
<div class="abs captcha">egTqU</div>
<div class="abs submit">SUBMIT</div>
<div class="abs lbl" style="left:33px;top:1056px">See Terms &amp; Conditions &nbsp;| &nbsp;FAQ's</div>
<p class="abs footnotes">*self employed or graduate student staying longer than one month: please provide proof of income.<br>** While we attempt to provide you with the apartment of your choice, we reserve the right to assign any similarly priced available apartment</p>

<div class="abs divider"></div>

<h2 class="abs heading" style="left:535px;top:565px">Quick Links</h2>
<svg width="0" height="0" style="position:absolute"><defs><path id="tick" d="M1 7l4 4L14 1" stroke="#c9b27a" stroke-width="3" fill="none"/></defs></svg>
<div class="abs quick" style="left:537px;top:612px"><svg width="16" height="14"><use href="#tick"/></svg>Links</div>
<div class="abs quick" style="left:537px;top:633px"><svg width="16" height="14"><use href="#tick"/></svg>Location</div>
<div class="abs quick" style="left:537px;top:654px"><svg width="16" height="14"><use href="#tick"/></svg>Rates</div>
<div class="abs quick" style="left:685px;top:612px"><svg width="16" height="14"><use href="#tick"/></svg>Blog</div>
<div class="abs quick" style="left:685px;top:633px"><svg width="16" height="14"><use href="#tick"/></svg>Chirper</div>
<div class="abs quick" style="left:685px;top:654px"><svg width="16" height="14"><use href="#tick"/></svg>Reviews</div>
<div class="abs rule" style="top:696px"></div>

<h2 class="abs heading" style="left:535px;top:715px">Client’s Testimonials</h2>
<article class="testimonial" style="top:761px">
  <div class="photo"><span role="img" aria-label="Portrait of a guest"></span></div>
  <div class="t-title">Lorem ipsum dolor</div>
  <p class="t-body">sit amet, consectetuer. Ut wisi enim ad minim veniam, quis nostrud exerci tation ullamcorper suscipit ndrerit in vulputatelestie consequat.</p>
  <div class="t-meta">5 days ago By Tomas Reed</div><div class="t-more">Read More</div>
</article>
<div class="abs rule" style="top:869px"></div>
<article class="testimonial" style="top:887px">
  <div class="photo"><span role="img" aria-label="Portrait of a guest"></span></div>
  <div class="t-title">Lorem ipsum dolor</div>
  <p class="t-body">sit amet, consectetuer. Ut wisi enim ad minim veniam, quis nostrud exerci tation ullamcorper suscipit ndrerit in vulputatelestie consequat.</p>
  <div class="t-meta">5 days ago By Tomas Reed</div><div class="t-more">Read More</div>
</article>
<div class="abs rule" style="top:994px"></div>
<article class="testimonial" style="top:1007px">
  <div class="photo"><span role="img" aria-label="Portrait of a guest"></span></div>
  <div class="t-title">Lorem ipsum dolor</div>
  <p class="t-body">sit amet, consectetuer. Ut wisi enim ad minim veniam, quis nostrud exerci tation ullamcorper suscipit ndrerit in vulputatelestie consequat.</p>
  <div class="t-meta">5 days ago By Tomas Reed</div><div class="t-more">Read More</div>
</article>

<footer>
  <div class="abs footer"></div>
  <div class="abs footer-text">RIBTEN LOFTS &nbsp;© 2012 Privacy Policy</div>
  <div class="abs social" style="left:618px;border-radius:50%;width:62px;background:#222"></div>
  <div class="abs social" style="left:697px;background:#3b5fa8"></div>
  <div class="abs social" style="left:763px;background:#4aa6d9"></div>
</footer>
</body>
</html>
```